Tea box package for Herbal Teas

We would like a design for a package of our tea products. We want the consumer to understand that our products are natural just by looking at the package. We prefer minimalistic designs.
The package we want would be a square (or slightly rectangular) box. The box would be generic enough for us to use it for different teas. Essentially what we want is all the main information and designs to be the same for each tea product we have. We would like to be able to change the main color and the name of the tea then to customize to the tea in the package. Please see the attached images for examples.
We really like the package in tea_packaging_example_4 picture. We would like our packaging to be something very similar but with all the labels printed on the package.
We already have our logo so I am attaching that as well (image named 'velk ansary logo copy'). That would go on the front of the box.
We also attach a tile created using our logo (see image called 'tile'). We would like this to go to the sides similarly to tea_packaging_example_4.
On the back of the pouch, we want to have directions on how to make the tea but we want this section to be editable. For now just 3-4 lines of sample text is fine along with instructions on how to make a tea, see picture 'back of tea box'.
We would like for the box color to be as in example picture
tea_packaging_example_4. The color of the writing should be the same as the logo color. The font style should be something that would look nice next to the logo font, we are not sure what that font should be. The only thing colored would be the name of the tea and the ribbon as seen in tea_packaging_example_4, which we would like to change if we need to, to other variations.
Thanks a lot. For any questions, please contact me.

```html
<!DOCTYPE html>
<html lang="en">
<head>
<meta charset="utf-8">
<title>Velk Ansary – Health Premium Tea box dieline</title>
<link href="https://fonts.googleapis.com/css2?family=Cormorant+Garamond:ital,wght@0,500;1,500&family=Montserrat:wght@400&family=Arimo:wght@400;700&display=swap" rel="stylesheet">
<style>
  :root{
    --gold:#e5bd69;
    --ink:#231f20;
    --ribbon:#2a8660;
    --paper:#ffffff;
    --tile-warm:#6e5832;
  }
  *{box-sizing:border-box;margin:0;padding:0}
  html,body{width:1200px;height:848px;overflow:hidden;background:#fff}
  .canvas{position:relative;width:1200px;height:848px}
  .dieline{position:absolute;left:0;top:0}

  .tile-field{position:absolute;width:204px;height:203px;
    background:radial-gradient(circle at 50% 50%,var(--tile-warm) 0%,#4a3c28 55%,var(--ink) 100%)}

  .brand-name{position:absolute;left:334px;width:234px;text-align:center;
    font-family:"Cormorant Garamond",serif;font-weight:500;font-size:21px;line-height:24px;
    letter-spacing:1px;color:var(--ink);text-transform:uppercase}

  .tea-name{position:absolute;left:334px;width:234px;text-align:center;color:var(--paper)}
  .tea-name__title{font-family:"Cormorant Garamond",serif;font-style:italic;font-weight:500;font-size:23px;line-height:22px}
  .tea-name__sub{font-family:"Montserrat",sans-serif;font-size:9.6px;line-height:10px;letter-spacing:5px;padding-left:5px;margin-top:4px}

  .howto{position:absolute;left:862px;width:246px;top:387px;text-align:center;color:var(--paper);
    font-family:"Arimo",sans-serif;font-size:9.6px;line-height:14.4px}
  .howto__title{font-weight:700}
</style>
</head>
<body>
<main class="canvas">

  <svg class="dieline" width="1200" height="848" viewBox="0 0 1200 848" aria-hidden="true">
    <defs>
      <clipPath id="flap-label-shape">
        <path d="M344 40H558V50H568V262H558V272H344V262H334V50H344Z"/>
      </clipPath>
      <clipPath id="front-label-shape">
        <path d="M344 309H558V319H568V524H558V534H344V524H334V319H344Z"/>
      </clipPath>
    </defs>

    <!-- flaps -->
    <rect x="318" y="22" width="267" height="268" fill="var(--gold)"/>
    <rect x="318" y="554" width="267" height="268" fill="var(--gold)"/>

    <!-- wrap band: four faces -->
    <rect x="51" y="289" width="1067" height="266" fill="var(--ink)"/>
    <g fill="var(--gold)">
      <rect x="57" y="295" width="256" height="254"/>
      <rect x="323" y="295" width="257" height="254"/>
      <rect x="590" y="295" width="256" height="254"/>
      <rect x="856" y="295" width="256" height="254"/>
    </g>
    <g fill="var(--ink)">
      <rect x="57" y="295" width="7" height="7"/><rect x="306" y="295" width="7" height="7"/>
      <rect x="57" y="542" width="7" height="7"/><rect x="306" y="542" width="7" height="7"/>
      <rect x="323" y="295" width="7" height="7"/><rect x="573" y="295" width="7" height="7"/>
      <rect x="323" y="542" width="7" height="7"/><rect x="573" y="542" width="7" height="7"/>
      <rect x="590" y="295" width="7" height="7"/><rect x="839" y="295" width="7" height="7"/>
      <rect x="590" y="542" width="7" height="7"/><rect x="839" y="542" width="7" height="7"/>
      <rect x="856" y="295" width="7" height="7"/><rect x="1105" y="295" width="7" height="7"/>
      <rect x="856" y="542" width="7" height="7"/><rect x="1105" y="542" width="7" height="7"/>
    </g>

    <!-- top flap label -->
    <rect x="350" y="22" width="202" height="18" fill="var(--ribbon)"/>
    <g clip-path="url(#flap-label-shape)">
      <rect x="334" y="40" width="234" height="180" fill="var(--paper)"/>
      <rect x="334" y="220" width="234" height="5" fill="var(--ink)"/>
      <rect x="334" y="225" width="234" height="47" fill="var(--ribbon)"/>
    </g>
    <path d="M344 40H558V50H568V262H558V272M344 272V262H334V50H344V40" fill="none" stroke="var(--ink)" stroke-width="2"/>
    <rect x="350" y="272" width="202" height="38" fill="var(--ribbon)"/>

    <!-- front label -->
    <g clip-path="url(#front-label-shape)">
      <rect x="334" y="309" width="234" height="165" fill="var(--paper)"/>
      <rect x="334" y="474" width="234" height="4" fill="var(--ink)"/>
      <rect x="334" y="478" width="234" height="56" fill="var(--ribbon)"/>
    </g>
    <path d="M350 309H344V319H334V524H344V534H558V524H568V319H558V309H552" fill="none" stroke="var(--ink)" stroke-width="2"/>

    <!-- label corner keys -->
    <g stroke="var(--ink)" stroke-width="1.4">
      <rect x="337" y="43" width="5" height="5" fill="var(--paper)"/>
      <rect x="560" y="43" width="5" height="5" fill="var(--paper)"/>
      <rect x="337" y="264" width="5" height="5" fill="var(--ribbon)"/>
      <rect x="560" y="264" width="5" height="5" fill="var(--ribbon)"/>
      <rect x="337" y="312" width="5" height="5" fill="var(--paper)"/>
      <rect x="560" y="312" width="5" height="5" fill="var(--paper)"/>
      <rect x="337" y="526" width="5" height="5" fill="var(--ribbon)"/>
      <rect x="560" y="526" width="5" height="5" fill="var(--ribbon)"/>
    </g>

    <!-- back panel -->
    <rect x="884" y="289" width="200" height="13" fill="var(--ribbon)"/>
    <path d="M871 302H1099V311H1108V532H1099V541H871V532H862V311H871Z" fill="var(--ink)"/>
    <g fill="var(--ink)">
      <rect x="874" y="307" width="5" height="5"/><rect x="1091" y="307" width="5" height="5"/>
      <rect x="874" y="531" width="5" height="5"/><rect x="1091" y="531" width="5" height="5"/>
    </g>
    <path d="M887 314H1083V322H1092V521H1083V529H887V521H878V322H887Z" fill="none" stroke="var(--gold)" stroke-width="1.2"/>
    <g fill="none" stroke="var(--gold)" stroke-width="1.2">
      <rect x="880" y="316" width="5" height="5"/><rect x="1085" y="316" width="5" height="5"/>
      <rect x="880" y="522" width="5" height="5"/><rect x="1085" y="522" width="5" height="5"/>
    </g>

    <!-- brewing icon -->
    <g fill="none" stroke="var(--ribbon)" stroke-width="1.6" stroke-linecap="round" transform="translate(968 342)">
      <path d="M14 6c-3 3 3 5 0 8M20 3c-3 3 3 5 0 8M26 6c-3 3 3 5 0 8"/>
      <path d="M6 18h26v6a13 11 0 0 1-26 0z"/>
      <path d="M32 20h3a3 3 0 0 1 0 6h-3"/>
      <path d="M4 36h32"/>
    </g>
  </svg>

  <!-- side faces -->
  <div class="tile-field" role="img" aria-label="Repeating gold and black tile pattern built from the brand emblem" style="left:83px;top:321px"></div>
  <div class="tile-field" role="img" aria-label="Repeating gold and black tile pattern built from the brand emblem" style="left:616px;top:321px"></div>

  <!-- brand and tea name -->
  <div class="brand-name" style="top:118px">Velk Ansary</div>
  <div class="tea-name" style="top:239px">
    <div class="tea-name__title">Health</div>
    <div class="tea-name__sub">PREMIUM TEA</div>
  </div>

  <div class="brand-name" style="top:380px">Velk Ansary</div>
  <div class="tea-name" style="top:491px">
    <div class="tea-name__title">Health</div>
    <div class="tea-name__sub">PREMIUM TEA</div>
  </div>

  <!-- back instructions -->
  <div class="howto">
    <div class="howto__title">How to make a tea:</div>
    <div>Eruptia elibusdae endere latis si<br>volor a descius ea sed ex eicium<br>autem volum quiam quiatiusdae</div>
  </div>

</main>
</body>
</html>
```